Business Card Design

6 piece Rock and Roll Cover band playing music from the 60's to present. We've got "The Wrens" as 2 lead vocalists singing anyone from the Copper Lanterns and Marigold to Velvet harbor ensemble and paper tigers through the The Amber Wolves. we play some bluesy country songs like those by the Lantern Sisters and Hollis Varney. We are based out of Camden, ME and are interested in venues that like to dance and party.
Our Design includes a western looking cartoon Pistol with smoke rolling out of the barrel as in - "nothing's sweeter than a rusty old Fiddle (borrowed)" We like Grays and greens with some hints of yellow and white
Target Market(s)
ages 25-30
Industry/Entity Type
Business
Contact Information for Business Card
RUSTY OLD FIDDLE
fanpage.net/rustyoldfiddleharbor
rustyold@rustyoldfiddleharbor.com
Look and feel

```html
<!DOCTYPE html>
<html lang="en">
<head>
<meta charset="utf-8">
<title>Rusty Old Fiddle – Business Card</title>
<link rel="stylesheet" href="https://fonts.googleapis.com/css2?family=Stardos+Stencil:wght@700&family=Montserrat:wght@300;400&display=swap">
<style>
  :root {
    --backdrop: #1c1c1c;
    --card-green: #2a302c;
    --band-red: #d42027;
    --band-gray: #4a4a4a;
    --title-gray: #a6a6a6;
    --icon-gray: #8f8f8f;
    --tagline: #d9d9d9;
    --accent-red: #d42027;
  }
  * { box-sizing: border-box; margin: 0; padding: 0; }
  html, body { width: 1200px; height: 800px; overflow: hidden; background: var(--backdrop); }
  .canvas { position: relative; width: 1200px; height: 800px; }
  .card {
    position: absolute; left: 100px; top: 110px;
    width: 1000px; height: 580px;
    background: var(--card-green);
    overflow: hidden;
  }
  .vertical { writing-mode: vertical-rl; }
  .brand-band {
    position: absolute; left: 0; top: 0; width: 125px; height: 100%;
    background: var(--band-red);
    display: flex; align-items: center; justify-content: center;
  }
  .band-title {
    font-family: "Stardos Stencil", serif; font-weight: 700;
    font-size: 40px; letter-spacing: 3px; color: var(--title-gray);
  }
  .contact {
    position: absolute; left: 258px; top: 18px;
    display: flex; flex-direction: column; align-items: center; gap: 14px;
  }
  .contact-icons { display: flex; gap: 2px; }
  .contact-lines {
    font-family: "Montserrat", sans-serif; font-weight: 400;
    font-size: 21px; line-height: 34px; letter-spacing: 1px;
    color: var(--accent-red);
  }
  .headline-band {
    position: absolute; left: 490px; top: 0; width: 130px; height: 100%;
    background: var(--band-gray);
    display: flex; justify-content: center; padding-top: 26px;
  }
  .headline { display: flex; flex-direction: column; align-items: center; }
  .headline-title {
    font-family: "Stardos Stencil", serif; font-weight: 700;
    font-size: 46px; letter-spacing: 3px; color: var(--accent-red);
    line-height: 60px;
  }
  .headline-tagline {
    font-family: "Montserrat", sans-serif; font-weight: 300;
    font-size: 17px; line-height: 24px; color: var(--tagline);
    text-align: center; margin-top: 26px;
  }
  .illustration {
    position: absolute; left: 665px; top: 70px; width: 300px; height: 430px;
    border-radius: 40px;
    background: radial-gradient(ellipse at 45% 45%, #a9c4d6 0%, #5f7f95 45%, #2f3f48 80%, rgba(42,48,44,0) 100%);
  }
</style>
</head>
<body>
<div class="canvas">
  <div class="card">
    <div class="brand-band">
      <div class="band-title vertical">RUSTY OLD FIDDLE</div>
    </div>

    <div class="contact">
      <div class="contact-icons">
        <svg width="40" height="44" viewBox="0 0 40 44" aria-label="email">
          <polygon points="20,1 38,11.5 38,32.5 20,43 2,32.5 2,11.5" fill="var(--icon-gray)"/>
          <rect x="10" y="15" width="20" height="14" fill="var(--accent-red)"/>
          <polyline points="10,15 20,23 30,15" fill="none" stroke="#f0f0f0" stroke-width="1.5"/>
        </svg>
        <svg width="40" height="44" viewBox="0 0 40 44" aria-label="fan page">
          <polygon points="20,1 38,11.5 38,32.5 20,43 2,32.5 2,11.5" fill="var(--icon-gray)"/>
        </svg>
      </div>
      <div class="contact-lines vertical">
        <p class="contact-social">fanpage.net/rustyoldfiddleharbor</p>
        <p class="contact-email">rustyold@rustyoldfiddleharbor.com</p>
      </div>
    </div>

    <div class="headline-band">
      <div class="headline vertical">
        <h1 class="headline-title">RUSTY OLD FIDDLE</h1>
        <p class="headline-tagline">Nothing's sweeter than a rusty old<br>Fiddle (borrowed)</p>
      </div>
    </div>

    <div class="illustration" role="img" aria-label="Cartoon western pistol illustration with a price tag and smoke from the barrel"></div>
  </div>
</div>
</body>
</html>
```